Modern Website Design for an Online Travel Agency.. Design Only!!

Hi there!

We are building an website for our travel agency that caters to tourists traveling to the Cayman Islands. We provide travel information and take bookings for various tours available here.

We need designs for 8 different web page layouts. You can see the layout specifications in two attached documents. We do not have a need for the coding to be done. This will simply act as a blueprint for our developer to build from.

The important pages are the 'Home Page' 'checkout page' and the ‘Checkout Page’ (Page 1 & 10 in the PDF ‘Website Layout’)

The MOST important page is ‘Tour Search Page’ (page 6)

If you intend on only submitting one page design, please submit a design for page 6. Be aware though, the more of these 3 page designs you submit, the more likely we are to move forward with you!

At this stage, we are simply looking to develop the most aesthetic website design layout possible.

- The website should be colour coordinated with the logo. You can most certainly use other colours if you feel they complement the overall design of the website well.

- Everything must be laid out in an EXTREMELY simple & ‘easy to navigate’ way. The key is simplicity & Functionality. There is no need for messy or elaborate graphics.

- The website MUST have a VERY clean and modern appearance.

- We want the main background to be white, but you can use light grey in places to compliment or add dimension if you feel necessary.

- We will appreciate a good use of shadows and especially a good use of icons. (You can see examples of icons we have already designed, we are definitely open to new icon design concepts too)

- We will reward imagination and original thinking! Essentially we want a website with a creative touch and unique design elements, whilst maintaining that clean and simple layout.

- Most importantly!! - Paying attention to the small details will be highly rewarded (A well balanced and seamless use of fonts, colours, dimensions, shadowing, positioning, etc)

If you have any questions, please don’t hesitate to ask.

We’re excited to see your design submissions!

Thank you!!

You can find all the support documents and content at: https://www.filevorra.net/sh/9qm2rtwplexan7c/QQBmTtZnPdLsWEGxvvaJpLmRw?dl=0

Target Market(s)

Tourists

Industry/Entity Type

Travel

Number of Pages Required

5+ page

Font styles to use
Sans Serif

Colors

Designer to choose colors to be used in the design.

Requirements
Must have
• Must be very clean and modern.
• Must be simple and bold
• Must be color coordinated in a way that makes sense
• White background
Nice to have
• Good use of shadows and Icons
Should not have
• Over use of messy graphics
• And design layout which is not right angled (using anything but vertical or horizontal for the edges in the design)

```html
<!DOCTYPE html>
<html lang="en">
<head>
<meta charset="utf-8">
<title>IsleRoute – Cayman Islands Travel</title>
<link href="https://fonts.googleapis.com/css2?family=Open+Sans:wght@300;400;600;700&family=Roboto:wght@400;500&display=swap" rel="stylesheet">
<style>
:root{
  --green:#8cc63e;--green-dark:#4f9a1c;--btn-top:#6cc232;--btn-bot:#3f8f14;
  --lime:#d6f53e;--blue:#3a70c0;--blue-text:#1c6fcc;--navy:#143a78;--navy-deep:#0f2e63;
  --sea-1:#2bb7c8;--sea-2:#0f8fa6;--sky:#3b8fd8;--red:#e3201b;
  --ink:#222;--muted:#555;--grey-bg:#f4f4f4;--pill:#cdd3de;--white:#fff;
}
*{box-sizing:border-box;margin:0;padding:0}
html,body{width:1200px;height:2956px;overflow:hidden}
body{font-family:"Open Sans",Arial,sans-serif;color:var(--ink);background:var(--white);position:relative}
.abs{position:absolute}
/* header */
.topbar{left:0;top:0;width:1200px;height:60px;background:var(--green)}
.social{right:168px;top:16px;display:flex;gap:10px}
.social span{width:28px;height:28px;border-radius:50%;background:#3d5a1c;display:block}
.login{right:100px;top:16px;width:80px;height:28px;background:#f2f2f2;border:1px solid #ccc;font-size:10px;color:#777;text-align:center;line-height:26px;letter-spacing:1px}
.mainnav{left:0;top:60px;width:1200px;height:48px;background:linear-gradient(#fff,#eceff3)}
.mainnav ul{position:absolute;left:410px;top:0;display:flex;list-style:none}
.mainnav li{height:48px;line-height:26px;padding-top:8px;font-size:13px;color:#333;text-align:center;border-left:1px solid #ccd;}
.infobar{left:0;top:108px;width:1200px;height:36px;background:linear-gradient(#4a80cf,#2f62b0)}
.infobar .cur{left:818px;top:8px;color:#fff;font-weight:700;font-size:13px}
.infobar .dest{left:950px;top:8px;color:var(--lime);font-weight:700;font-size:12px}
.infobar .dd{left:1073px;top:7px;width:22px;height:22px;background:var(--red);border-radius:3px}
.logo-panel{left:73px;top:0;width:278px;height:162px;background:#fff;box-shadow:0 3px 8px rgba(0,0,0,.25)}
.logo{left:12px;top:70px;display:flex;align-items:center;gap:8px}
.logo i{width:36px;height:36px;background:var(--green);display:block}
.logo b{font-size:33px;font-weight:700;color:var(--green-dark);letter-spacing:-.5px}
.backdrop{left:0;top:144px;width:1200px;height:772px;background:linear-gradient(120deg,#f7f7f7 0,#fff 30%,#efefef 60%,#fafafa 100%)}
/* slider */
.slider{left:89px;top:201px;width:1024px;height:382px;background:#fff;padding:5px;box-shadow:0 2px 8px rgba(0,0,0,.3)}
.photo{width:100%;height:100%;background:linear-gradient(#3a93dc 0,#8cc3ee 38%,#4e8f52 44%,#2ec1cd 52%,#13a0b4 100%)}
.slider h2{left:34px;top:22px;color:#fff;font-weight:400;font-size:33px;letter-spacing:3px}
.search{left:797px;top:318px;width:146px;height:42px;background:var(--red);color:#fff;font-size:15px;border-radius:2px;line-height:42px;text-align:center}
.dots{left:485px;top:346px;display:flex;gap:22px}
.dots span{width:12px;height:12px;border-radius:50%;background:#ddd;display:block}
.dots span:first-child{background:#444}
.arrow{top:380px;width:50px;height:50px;border-radius:50%;background:rgba(160,160,160,.85)}
/* about */
.h1{width:1200px;text-align:center;font-size:35px;font-weight:400;color:#111}
.about-text{left:128px;top:720px;width:944px;font-size:11.5px;line-height:18.5px;color:#222}
.btn{color:#fff;background:linear-gradient(var(--btn-top),var(--btn-bot));border-radius:3px;text-align:center;font-weight:600;box-shadow:0 2px 3px rgba(0,0,0,.2)}
.learn{left:128px;top:837px;width:114px;height:34px;line-height:34px;font-size:12px}
.mapband{left:0;top:916px;width:1200px;height:404px;background:linear-gradient(#1f6ec7 0,#7db6e6 45%,#567c4a 52%,#2ac0cc 60%,#0f8ea6 100%)}
.mapband h2{top:32px;width:1200px;text-align:center;color:#fff;font-weight:400;font-size:34px}
/* locations */
.loc{top:1426px;height:46px;line-height:46px;font-size:16px;font-weight:400}
.loc b{font-weight:700}
.small-center{width:1200px;text-align:center;font-size:15px;line-height:28px;color:#222}
/* things to do */
.things{left:87px;top:1619px;width:1026px;height:800px;background:linear-gradient(#fafafa,#f1f1f1);border:1px solid #ddd;box-shadow:0 6px 10px rgba(0,0,0,.18)}
.pill{left:15px;top:40px;width:994px;height:47px;background:var(--pill);border-radius:24px;text-align:center;line-height:47px;font-size:33px;letter-spacing:7px;color:#333;font-weight:300}
.video{top:202px;width:272px;height:207px;background:#fff;padding:4px;box-shadow:0 1px 4px rgba(0,0,0,.3)}
.video .v{width:100%;height:100%;background:linear-gradient(#8fbbe6 0,#cfe2f2 35%,#2f8cae 55%,#1d5f8e 100%);position:relative}
.video svg{position:absolute;left:116px;top:78px}
.card{top:462px;width:230px;height:283px;background:#fff;box-shadow:0 1px 5px rgba(0,0,0,.3)}
.card h3{height:65px;background:var(--lime);color:var(--blue-text);font-size:33px;font-weight:600;text-align:center;line-height:65px}
.card .ill{margin:14px;height:190px;background:linear-gradient(#eef5fb,#d8ecf5)}
.cta1{top:2468px;width:1200px;text-align:center;color:var(--blue-text);font-family:"Roboto",sans-serif;font-size:25px;font-weight:500}
.cta2{top:2508px;width:1200px;text-align:center;font-family:"Roboto",sans-serif;font-size:25px;color:#222}
/* footer */
.footer{left:0;top:2583px;width:1200px;height:323px;background:linear-gradient(110deg,var(--navy-deep) 0,var(--navy) 70%,#2a5399 100%);color:#c8d4ea}
.footer .flogo{left:108px;top:36px;display:flex;align-items:center;gap:8px}
.flogo i{width:34px;height:34px;background:var(--green);display:block}
.flogo b{font-size:30px;font-weight:700;color:var(--green)}
.footer p.desc{left:108px;top:96px;width:310px;font-size:10.5px;line-height:16px}
.contact{left:108px;font-size:11.5px;color:#fff;display:flex;align-items:center;gap:14px}
.footer h4{font-weight:400;color:#fff;font-size:18px}
.cats{left:453px;top:100px;width:112px;list-style:none}
.cats li{font-size:11.5px;color:#fff;height:31px;line-height:30px;border-bottom:1px solid #3d5c96}
.fphoto{left:601px;width:148px;height:96px;border-radius:12px}
.tweet{left:786px;display:flex;gap:22px;width:330px}
.tweet i{flex:none;width:34px;height:34px;border-radius:50%;background:#0d285a;display:block}
.tweet p{font-size:10.5px;line-height:15px}
.tweet small{display:block;color:#fff;font-size:10px;margin-top:6px}
.bottombar{left:0;top:2906px;width:1200px;height:50px;background:var(--green);font-size:11px;color:#1d2d10}
.bottombar .copy{left:108px;top:18px}
.bottombar ul{position:absolute;right:86px;top:18px;display:flex;gap:30px;list-style:none}
</style>
</head>
<body>

<div class="abs backdrop"></div>

<header>
  <div class="abs topbar">
    <div class="abs social"><span></span><span></span><span></span><span></span></div>
    <div class="abs login">LOGIN</div>
  </div>
  <nav class="abs mainnav">
    <ul>
      <li style="width:152px">DISCOVER CAYMAN</li>
      <li style="width:138px">TTHING TO DO</li>
      <li style="width:138px">MY TRIP PLANNER</li>
      <li style="width:138px">MAP</li>
      <li style="width:140px;border-right:1px solid #ccd">CONTACT US</li>
    </ul>
  </nav>
  <div class="abs infobar">
    <span class="abs cur">USD$</span>
    <span class="abs dest">Destinations [v]</span>
    <span class="abs dd"><svg width="22" height="22"><path d="M6 9h10l-5 6z" fill="#fff"/></svg></span>
  </div>
  <div class="abs logo-panel">
    <div class="abs logo"><i></i><b>IsleRoute</b></div>
  </div>
</header>

<section class="abs slider">
  <div class="photo" role="img" aria-label="Photo of a turquoise Caribbean sea with a palm-lined island shore"></div>
  <h2 class="abs">CAYMAN ISLANDS</h2>
  <div class="abs dots"><span></span><span></span><span></span><span></span><span></span></div>
  <div class="abs search">Search Now &nbsp;<svg width="14" height="12"><path d="M0 4h7V0l7 6-7 6V8H0z" fill="#fff"/></svg></div>
</section>
<div class="abs arrow" style="left:54px"><svg width="50" height="50"><path d="M29 15l-10 10 10 10" stroke="#fff" stroke-width="3" fill="none"/></svg></div>
<div class="abs arrow" style="left:1098px"><svg width="50" height="50"><path d="M21 15l10 10-10 10" stroke="#fff" stroke-width="3" fill="none"/></svg></div>

<section>
  <h2 class="abs h1" style="top:630px">About the Cayman Islands</h2>
  <p class="abs about-text">We are proud travel concierges of the Cayman Islands! We help thousands of tourists visiting Cayman every year arrange vacation getaway catered to their exact needs. With a wealth of local knowledge, we help you avoid unreliable tour operators and find those local hidden gems. Here you can research everything you need to be fully prepared for your travelsandalso view the complete range of activities available. &nbsp;Once you're ready to move forward, we'll help you fine tune your itinerary and continue to make all the booking arrangements on your behalf. All of our services are <b>100% FREE</b> with <b>No Hidden Costs</b>. Meaning you pay exactly the same prices asthough you were booking directly with the tour operators yourself.</p>
  <div class="abs btn learn">Learn more</div>
</section>

<section class="abs mapband" role="img" aria-label="Photo of the island coastline with clear blue water, used as the activities map banner">
  <h2 class="abs">Activities Map</h2>
</section>

<section>
  <h2 class="abs h1" style="top:1352px">Locations</h2>
  <div class="abs btn loc" style="left:85px;width:236px">RUM POINT: <b>24 Activities</b></div>
  <div class="abs btn loc" style="left:347px;width:231px">EAST END: <b>15 Activities</b></div>
  <div class="abs btn loc" style="left:597px;width:221px">WEST BAY: <b>4 Activities</b></div>
  <div class="abs btn loc" style="left:839px;width:274px">GEORGE TOWN: <b>39 Activities</b></div>
  <p class="abs small-center" style="top:1504px">Lorem ipsum dolor sit amet, consectetur adipiscing elit, sed do eiusmod tempor incididunt ut labore et dolore magna aliqua.<br>Ut enim ad minim veniam, quis nostrud exercitation ullamco laboris nisi ut aliquip ex ea commodo consequat.</p>
</section>

<section class="abs things">
  <div class="abs pill">THINGS TO DO’</div>
  <p class="abs small-center" style="left:-87px;top:112px">Lorem ipsum dolor sit amet, consectetur adipiscing elit, sed do eiusmod tempor incididunt ut labore et dolore magna aliqua.<br>Ut enim ad minim veniam, quis nostrud exercitation ullamco laboris nisi ut aliquip ex ea commodo consequat.</p>
  <svg class="abs" style="left:14px;top:292px" width="30" height="62"><path d="M26 2L4 31l22 29" stroke="#aaa" stroke-width="7" fill="none"/></svg>
  <svg class="abs" style="left:978px;top:292px" width="30" height="62"><path d="M4 2l22 29L4 60" stroke="#1a3d80" stroke-width="7" fill="none"/></svg>
  <div class="abs video" style="left:65px"><div class="v" role="img" aria-label="Video still: aerial view of the island and reef"><svg width="40" height="44"><path d="M2 2l36 20L2 42z" fill="#fff"/></svg></div></div>
  <div class="abs video" style="left:366px"><div class="v" role="img" aria-label="Video still: aerial view of the island and reef"><svg width="40" height="44"><path d="M2 2l36 20L2 42z" fill="#fff"/></svg></div></div>
  <div class="abs video" style="left:670px"><div class="v" role="img" aria-label="Video still: aerial view of the island and reef"><svg width="40" height="44"><path d="M2 2l36 20L2 42z" fill="#fff"/></svg></div></div>
  <div class="abs card" style="left:15px"><h3>Explore</h3><div class="ill" role="img" aria-label="Illustration of a traveller browsing destinations beside luggage"></div></div>
  <div class="abs card" style="left:270px"><h3>Choose</h3><div class="ill" role="img" aria-label="Illustration of a person choosing activities on a laptop"></div></div>
  <div class="abs card" style="left:524px"><h3>Arrange</h3><div class="ill" role="img" aria-label="Illustration of travellers arranging their trip with a suitcase"></div></div>
  <div class="abs card" style="left:780px"><h3>Relax</h3><div class="ill" role="img" aria-label="Illustration of people relaxing on the beach"></div></div>
</section>

<p class="abs cta1">Don’t miss out on the best activities because you waited last minute.</p>
<p class="abs cta2">Contact Us now to see how we can help you put together your perfect vacation getaway!</p>

<footer class="abs footer">
  <div class="abs flogo"><i></i><b>IsleRoute</b></div>
  <p class="abs desc">Lorem Ipsum is simply dummy text of the printing and typesetting industry. Lorem Ipsum has been the industry's standard dummy text ever since the 1500s, when an unknown printer took a galley of type and scrambled it to make a type specimen book. It has</p>
  <div class="abs contact" style="top:206px"><svg width="14" height="14"><path d="M2 1v12M2 2h10l-3 3 3 3H2" stroke="#fff" fill="none" stroke-width="1.5"/></svg>Address 123, Country</div>
  <div class="abs contact" style="top:236px"><svg width="14" height="14"><rect x="3" y="1" width="8" height="12" rx="1" stroke="#fff" fill="none" stroke-width="1.5"/></svg>(555) 010-4827</div>
  <div class="abs contact" style="top:266px"><svg width="14" height="14"><rect x="1" y="3" width="12" height="8" stroke="#fff" fill="none" stroke-width="1.5"/><path d="M1 3l6 5 6-5" stroke="#fff" fill="none" stroke-width="1.2"/></svg>info@isleroute-mail.net</div>
  <h4 class="abs" style="left:453px;top:58px">Categories</h4>
  <ul class="abs cats"><li>Discover Cayman</li><li>Thing to Do</li><li>My Trip Planner</li><li>Map</li><li>Contact Us</li></ul>
  <div class="abs fphoto" style="top:58px;background:linear-gradient(#7fb7e4,#d9b99a 55%,#2bb5c6)" role="img" aria-label="Photo of a person jumping on the beach"></div>
  <div class="abs fphoto" style="top:162px;background:linear-gradient(#3bb3b8,#1e8c96)" role="img" aria-label="Photo of snorkelers in clear water"></div>
  <svg class="abs" style="left:664px;top:264px" width="22" height="12"><path d="M2 10l9-8 9 8" stroke="#6f87b5" stroke-width="3" fill="none"/></svg>
  <h4 class="abs" style="left:784px;top:58px">Latest Posts</h4>
  <div class="abs tweet" style="top:100px"><i></i><p>Lorem ipsum dolor sit amet, consectetur adipiscing elit, sed do eiusmod tempor incididunt ut labore et dolore.<small>2 hours ago</small></p></div>
  <div class="abs tweet" style="top:172px"><i></i><p>Lorem ipsum dolor sit amet, consectetur adipiscing elit, sed do eiusmod tempor incididunt ut labore et dolore.<small>2 hours ago</small></p></div>
  <div class="abs tweet" style="top:244px"><i></i><p>Lorem ipsum dolor sit amet, consectetur adipiscing elit, sed do eiusmod tempor incididunt ut labore et dolore.<small>2 hours ago</small></p></div>
</footer>

<div class="abs bottombar">
  <span class="abs copy">Copyrights. © 2019 by ISLEROUTE</span>
  <ul><li>Home</li><li>My Cart</li><li>Checkout</li><li>Completed Orders</li><li>Contact us</li></ul>
</div>

</body>
</html>
```